Ember Ridge Clearing postcard ( for direct mailing) and business card design

Design postcards/Business cards
Dale Horvick
Ember Ridge Clearing
482 Copperfern Rd Lewisville,NC 27023
(336) 555-0184 Dale@Emberridgeclearing.example

The postcard will be used for direct mailing to land owners and contractors to advertise our service. Pictures of the process and equipment along with a short summary of what we do. Business card should be contact info and logo.
Updates

The post cards could say something like this: Forestry Mulching machines are capable of clearing land of unwanted trees and brush with limited disturbance to soils or desirable vegetation. Traditional land clearing methods often present an increased risk of erosion by pushing over trees, uprooting the stump and roots, and substantially disturbing soils.In contrast, mulching the vegetation leaves the soil structure intact. The mulched material can be left on the ground and will act as an erosion barrier while returning nutrients back into the soil through decomposition. Over time, grass will naturally grow through the mulch and can be maintained with mowing.

Target Market(s)

Land owners and contractors who need vegetation cleared

Industry/Entity Type

Forestry Mulching

Requirements
Must have
• picture, brief description of service offered, contact info on postcard. Business card should have contact info and logo.
Nice to have
• I like contour lines as a background but I'd like to see other ideas.

```html
<!DOCTYPE html>
<html lang="en">
<head>
<meta charset="utf-8">
<title>Ember Ridge Clearing – Business Card</title>
<link href="https://fonts.googleapis.com/css2?family=Montserrat:wght@400;600;700;800&display=swap" rel="stylesheet">
<style>
  :root {
    --page: #ffffff;
    --ink: #111111;
    --card-dark: #0c0d0d;
    --card-light: #ffffff;
    --green-deep: #1a7a38;
    --green-mid: #2f9e48;
    --green-lime: #8cc63f;
    --rule: #b5b5b5;
    --text: #333333;
  }
  * { box-sizing: border-box; margin: 0; padding: 0; }
  html, body {
    width: 687px; height: 1200px; overflow: hidden;
    background: var(--page);
    font-family: "Montserrat", sans-serif;
  }
  .sheet {
    position: relative; width: 687px; height: 1200px;
  }
  .card {
    position: absolute; left: 60px; width: 566px; height: 324px;
    overflow: hidden;
    box-shadow: 0 3px 10px rgba(0,0,0,0.22);
  }
  .card--back { top: 252px; background: var(--card-dark); }
  .card--front { top: 624px; background: var(--card-light); }

  .contour-field {
    position: absolute;
  }
  .card--back .contour-field {
    inset: 0;
    background: radial-gradient(ellipse at 65% 40%, rgba(60,80,60,0.28), rgba(0,0,0,0) 70%);
  }
  .card--front .contour-field {
    left: 222px; top: 0; width: 344px; height: 162px;
    background: radial-gradient(ellipse at 70% 35%, rgba(140,198,63,0.12), rgba(255,255,255,0) 70%);
  }

  .wordmark {
    position: absolute; display: flex; align-items: center; gap: 14px;
  }
  .wordmark__square {
    width: 36px; height: 36px; background: var(--green-mid); flex: none;
  }
  .wordmark__name {
    font-weight: 800; text-transform: uppercase; letter-spacing: 1px;
    line-height: 1.02;
  }
  .card--back .wordmark { left: 150px; top: 116px; }
  .card--back .wordmark__name { color: #ffffff; font-size: 27px; }
  .card--front .wordmark { left: 20px; top: 46px; }
  .card--front .wordmark__name { color: var(--ink); font-size: 27px; }

  .holder {
    position: absolute; right: 20px; top: 164px;
    display: flex; align-items: center; gap: 8px;
    font-weight: 700; font-size: 25px; color: var(--ink);
  }
  .holder svg { width: 16px; height: 18px; }
  .rule {
    position: absolute; left: 18px; right: 19px; top: 202px;
    height: 1.5px; background: var(--rule);
  }
  .contacts {
    position: absolute; left: 18px; top: 218px; list-style: none;
    font-size: 14px; color: var(--text); letter-spacing: 0.4px;
  }
  .contacts li { display: flex; align-items: center; gap: 11px; height: 22.5px; }
  .contacts svg { width: 15px; height: 15px; flex: none; }
  .contacts strong { font-weight: 700; }
  .address {
    position: absolute; left: 412px; top: 226px;
    display: flex; gap: 11px;
    font-size: 14px; line-height: 18px; color: var(--text); letter-spacing: 0.4px;
  }
  .address svg { width: 13px; height: 18px; margin-top: 2px; flex: none; }
  .bands { position: absolute; left: 0; bottom: 0; width: 566px; height: 20px; }
</style>
</head>
<body>
<main class="sheet">

  <section class="card card--back" aria-label="Business card back">
    <div class="contour-field" role="img" aria-label="Faint topographic contour lines across the dark background"></div>
    <div class="wordmark">
      <span class="wordmark__square"></span>
      <span class="wordmark__name">Ember Ridge<br>Clearing</span>
    </div>
  </section>

  <section class="card card--front" aria-label="Business card front">
    <div class="contour-field" role="img" aria-label="Pale green topographic contour lines in the upper right"></div>
    <div class="wordmark">
      <span class="wordmark__square"></span>
      <span class="wordmark__name">Ember Ridge<br>Clearing</span>
    </div>

    <div class="holder">
      <svg viewBox="0 0 16 18" aria-hidden="true"><circle cx="8" cy="5" r="4.2" fill="var(--green-mid)"/><path d="M0 18c0-5 3.5-7.5 8-7.5s8 2.5 8 7.5z" fill="var(--green-deep)"/></svg>
      Dale Horvick
    </div>
    <div class="rule"></div>

    <ul class="contacts">
      <li>
        <svg viewBox="0 0 16 16" aria-hidden="true"><path d="M3.5 1.5l2.5 3-1.6 1.6c.9 2 2.5 3.6 4.5 4.5L10.5 9l3 2.5-1.6 2.7C6.8 14 2 9.2 1.8 3.2z" fill="none" stroke="var(--green-mid)" stroke-width="1.6" stroke-linejoin="round"/></svg>
        (336) 555-0184
      </li>
      <li>
        <svg viewBox="0 0 16 16" aria-hidden="true"><rect x="1" y="3" width="14" height="10" fill="var(--green-mid)"/><path d="M1 3l7 6 7-6" fill="none" stroke="#fff" stroke-width="1.2"/></svg>
        Dale@Emberridgeclearing.example
      </li>
      <li>
        <svg viewBox="0 0 16 16" aria-hidden="true"><circle cx="8" cy="8" r="6.5" fill="none" stroke="var(--green-mid)" stroke-width="1.5"/><ellipse cx="8" cy="8" rx="2.8" ry="6.5" fill="none" stroke="var(--green-mid)" stroke-width="1.2"/><path d="M1.5 8h13M2.5 5h11M2.5 11h11" stroke="var(--green-mid)" stroke-width="1.1"/></svg>
        <span>www.<strong>Emberridgeclearing</strong>.example</span>
      </li>
    </ul>

    <div class="address">
      <svg viewBox="0 0 13 18" aria-hidden="true"><path d="M6.5 17C2.5 11.5 1 9 1 6.5a5.5 5.5 0 0 1 11 0C12 9 10.5 11.5 6.5 17z" fill="var(--green-mid)"/><circle cx="6.5" cy="6.5" r="2" fill="#fff"/></svg>
      <p>482 Copperfern<br>Rd Lewisville,<br>NC 27023</p>
    </div>

    <svg class="bands" viewBox="0 0 566 20" preserveAspectRatio="none" aria-hidden="true">
      <polygon points="0,10 364,10 358,20 0,20" fill="var(--green-mid)"/>
      <polygon points="0,15 361,15 358,20 0,20" fill="var(--green-deep)"/>
      <polygon points="374,0 566,0 566,20 363,20" fill="var(--green-lime)"/>
    </svg>
  </section>

</main>
</body>
</html>
```